Butcher shop

We have 2 butcher shops:

Shop 9, Ridgeway Court, Aberdeen NSW 2336
Ph 02 6512 3840

47 Marlow St, Scone NSW 2337
Ph 02 6518 2274

ABN 48 907 215 816

I would like this info on reverse of card and my personal info on front of card. I have a logo I would like to use also. Require a very smooth thick matte card, with colour both sides.

Front of card should say:

Linda Farrugia
Accounts

Ph 0437 620 915
E lindafarrugia@quollmail.com.au

Industry/Entity Type

Shop

Contact Information for Business Card

Linda Farrugia
Ph 0437 620 915

Logo Text

Farrugia's Quality Meats

Logo styles of interest
Pictorial/Combination Logo
Requirements
Must have
• We use Century Gothic Font

```html
<!DOCTYPE html>
<html lang="en">
<head>
<meta charset="utf-8">
<title>Farrugia's Quality Meats – Business Card</title>
<link rel="stylesheet" href="https://fonts.googleapis.com/css2?family=Questrial&display=swap">
<style>
  :root {
    --card-light: #e8dbad;
    --card-mid: #dcc890;
    --card-dark: #c4a868;
    --ink: #1d221f;
    --frame: #2a2a24;
  }
  html, body {
    margin: 0;
    padding: 0;
    width: 1200px;
    height: 693px;
    overflow: hidden;
    background: var(--card-dark);
  }
  .card {
    position: relative;
    width: 1200px;
    height: 693px;
    overflow: hidden;
    font-family: "Questrial", "Century Gothic", sans-serif;
    color: var(--ink);
    background: radial-gradient(ellipse 70% 80% at 48% 40%, var(--card-light) 0%, var(--card-mid) 55%, var(--card-dark) 100%);
  }
  .texture {
    position: absolute;
    inset: 0;
    background: linear-gradient(135deg, rgba(255,255,255,0.10) 0%, rgba(255,255,255,0) 40%, rgba(0,0,0,0.04) 100%);
  }
  .brand-name {
    position: absolute;
    left: 0;
    width: 1200px;
    top: 205px;
    margin: 0;
    text-align: center;
    font-weight: 400;
    font-size: 50px;
    line-height: 59px;
    letter-spacing: 0.5px;
  }
  .tagline {
    position: absolute;
    left: 0;
    width: 1186px;
    top: 352px;
    margin: 0;
    text-align: center;
    font-style: italic;
    font-size: 37px;
    line-height: 44px;
    letter-spacing: 2px;
  }
  .contact-box {
    position: absolute;
    left: 229px;
    top: 424px;
    width: 768px;
    height: 210px;
    box-sizing: border-box;
    border: 1px solid var(--frame);
    padding-top: 11px;
    text-align: center;
    font-size: 36px;
    line-height: 45px;
    letter-spacing: 1.5px;
  }
  .contact-box p { margin: 0; white-space: nowrap; }
</style>
</head>
<body>
  <main class="card">
    <div class="texture"></div>
    <h1 class="brand-name">Farrugia's<br>Quality Meats</h1>
    <p class="tagline">Fresh cut meats and poultry</p>
    <section class="contact-box">
      <p class="person-name">Linda Farrugia</p>
      <p class="person-role">Accounts</p>
      <p class="person-phone">Tel;- 0437 620 915</p>
      <p class="person-email">E-mail: lindafarrugia@quollmail.com.au</p>
    </section>
  </main>
</body>
</html>
```